Vell Partners Building Business Cards

We need a business card that reflects our business as "Solar Experts" in San Diego. Browse our website www.vellpartners.example our License needs to be displayed as "CSLB# 4718392" our phone number is (619) 555-0147

Save thousands on your electric bills and increase the value of your home while helping to protect the environment. Our solar installation experts will help you design the system that's right for you, using only the highest quality equipment that will look great and give you ideal performance. Our goal is to make you energy independent, and get your electric bill to 0.

Tobias Wrenfield
(619) 555-0147
tobias@vellpartners.example

Target Market(s)

Home owners in san diego looking for solar

Industry/Entity Type

Solar Energy

Contact Information for Business Card

Tobias Wrenfield
(619) 555-0147
tobias@vellpartners.example

Font styles to use
Other font styles liked:
• Use our logo font

Requirements
Must have
• License needs to be displayed as "CSLB# 4718392" our phone number is (619) 555-0147
Nice to have
• Real images of rooftop home solar in san diego
Should not have
• our business address

```html
<!DOCTYPE html>
<html lang="en">
<head>
<meta charset="utf-8">
<title>Vell Partners Building – Business Card</title>
<link rel="stylesheet" href="https://fonts.googleapis.com/css2?family=Source+Sans+3:ital,wght@0,400;0,600;0,700;1,400&display=swap">
<style>
  :root {
    --navy: #1b3d73;
    --gold: #f5a800;
    --ink: #3a3f47;
    --rule: #55607a;
    --paper: #ffffff;
    --backdrop: #d9dadc;
  }
  * { box-sizing: border-box; margin: 0; padding: 0; }
  html, body { width: 1105px; height: 1200px; overflow: hidden; }
  body {
    background: var(--backdrop);
    font-family: "Source Sans 3", sans-serif;
    position: relative;
  }
  .card {
    position: absolute;
    left: 193px;
    width: 719px;
    height: 411px;
    border-radius: 19px;
    overflow: hidden;
  }
  .card--front { top: 167px; background: var(--paper); }
  .card--back { top: 623px; background: var(--navy); }

  .brand {
    position: absolute;
    top: 46px;
    right: 47px;
    display: flex;
    align-items: center;
    gap: 10px;
  }
  .brand__mark {
    width: 22px; height: 22px;
    border-radius: 50%;
    background: var(--gold);
  }
  .brand__name {
    font-weight: 700;
    font-size: 36px;
    color: var(--navy);
    letter-spacing: -0.5px;
  }

  .person { position: absolute; left: 47px; top: 208px; }
  .person__name { font-size: 26px; font-weight: 600; color: var(--navy); line-height: 1.1; }
  .person__title { font-size: 19px; color: var(--gold); margin-top: 2px; }

  .rule {
    position: absolute;
    left: 47px; right: 47px; top: 276px;
    height: 1.5px;
    background: var(--rule);
  }

  .contacts {
    position: absolute;
    left: 47px; top: 292px;
    list-style: none;
  }
  .contacts li {
    display: flex; align-items: center; gap: 8px;
    font-size: 19px; color: var(--ink);
    height: 27.5px;
  }
  .contacts svg { width: 17px; height: 17px; fill: var(--navy); flex: none; }

  .license {
    position: absolute;
    right: 47px; top: 345px;
    font-size: 19px; color: var(--ink);
  }

  .edge-band { position: absolute; left: 0; bottom: 0; width: 100%; height: 12px; }

  .back-brand {
    position: absolute;
    left: 0; right: 0; top: 150px;
    display: flex; justify-content: center; align-items: center; gap: 14px;
  }
  .back-brand .brand__mark { width: 34px; height: 34px; }
  .back-brand .brand__name { color: var(--paper); font-size: 44px; }
  .back-url {
    position: absolute;
    left: 0; right: 0; top: 338px;
    text-align: center;
    font-style: italic;
    font-size: 21px;
    letter-spacing: 4px;
    color: var(--paper);
  }
</style>
</head>
<body>
  <section class="card card--front" aria-label="Business card front">
    <div class="brand">
      <span class="brand__name">Vell Partners Building</span>
    </div>

    <div class="person">
      <p class="person__name">Tobias Wrenfield</p>
      <p class="person__title">CEO/Founder</p>
    </div>

    <div class="rule"></div>

    <ul class="contacts">
      <li>
        <svg viewBox="0 0 24 24" aria-hidden="true"><path d="M6.6 10.8a15 15 0 0 0 6.6 6.6l2.2-2.2a1 1 0 0 1 1-.25 11.4 11.4 0 0 0 3.6.57 1 1 0 0 1 1 1V20a1 1 0 0 1-1 1A17 17 0 0 1 3 4a1 1 0 0 1 1-1h3.5a1 1 0 0 1 1 1c0 1.25.2 2.45.57 3.6a1 1 0 0 1-.25 1z"/></svg>
        (619) 555-0147
      </li>
      <li>
        <svg viewBox="0 0 24 24" aria-hidden="true"><path d="M2 5h20v14H2z M2 5l10 8 10-8" fill="var(--navy)"/><path d="M3 6l9 7 9-7" fill="none" stroke="#fff" stroke-width="1.6"/></svg>
        tobias@vellpartners.example
      </li>
      <li>
        <svg viewBox="0 0 24 24" aria-hidden="true"><circle cx="12" cy="12" r="10"/><path d="M2 12h20M12 2c3 3 3 17 0 20M12 2c-3 3-3 17 0 20" stroke="#fff" stroke-width="1.4" fill="none"/></svg>
        www.vellpartners.example
      </li>
    </ul>

    <p class="license">CSLB# 4718392</p>

    <svg class="edge-band" viewBox="0 0 719 12" preserveAspectRatio="none" aria-hidden="true">
      <polygon points="0,0 468,0 464,12 0,12" fill="var(--navy)"/>
      <polygon points="472,0 719,0 719,12 468,12" fill="var(--gold)"/>
    </svg>
  </section>

  <section class="card card--back" aria-label="Business card back">
    <div class="back-brand">
      <span class="brand__mark"></span>
      <span class="brand__name">Vell Partners Building</span>
    </div>
    <p class="back-url">www.vellpartners.example</p>
  </section>
</body>
</html>
```